依頼詳細
レスポンシブウェブデザインを意識したデザインでお願いします。

デザインに関しては、添付してあるデザインレイアウトシートを基にお願いします。
参考サイトのURLはデザインレイアウトシートに記載してあります。
色合いはグリーンかブルーを基調にお願いします。
新規のウェブサイトですので、既存サイトはありません。
ロゴも不要です。(後ではめ込むので社名だけテキストでレイアウトをお願いします。)
また、写真データも添付するので、レイアウトシートのイメージ画像に当て込んでください。

まずはパソコンサイトのデザインをお願いします。
当選後、スマホデザインをお願いします。

既存のテンプレートを使う場合は
テンプレート名を下記のような記載を提案の中にいれてください。
例:WordpressテーマはCorpLumen、デザインスキンは無料のQRN2019 LX4(http://corplumen.example/ex_plugin/qrnfuji2019_lx4/)をベースにデザインいたしました。
など

写真データで足りない場合は、一旦他のサイトや参考URLの写真をサンプルとして入れてください。(サンプルなどの表記をお願いします)
また、購入が必要な写真などを利用した場合は、Pixora Stock(https://stock.pixora-img.example/jp/)からファイル番号と価格を教えてください。
ページ数
1ページ
希望イメージ
シンプル 複雑
単色 カラフル
暗い 明るい
日常 高級
遊び心 厳粛
未来的 伝統的
女性的 男性的
希望する色
青系、緑系
納品ファイル
• イラストレーター形式 (.ai)
• フォトショップ形式 (.psd)
• PNG形式 (.png)
補足説明
上記のいずれか1つ。アウトラインありとなしの2つ。

こちらの要望を汲んで、デザインしていただきました。
ありがとうございました。

たくさんのご提案ありがとうございました。
次回もぜひ、よろしくお願い致します。

```html
<!DOCTYPE html>
<html lang="ja">
<head>
<meta charset="utf-8">
<title>有限会社青嶺</title>
<link rel="stylesheet" href="https://fonts.googleapis.com/css2?family=Noto+Serif+JP:wght@400;600&family=Noto+Sans+JP:wght@400;500&display=swap">
<style>
:root{
  --blue:#1478a8;
  --ink:#333333;
  --muted:#666666;
  --grey-bg:#ededed;
  --footer-bg:#e4e4e4;
  --white:#ffffff;
}
*{margin:0;padding:0;box-sizing:border-box}
html,body{width:1200px;height:3884px;overflow:hidden}
body{position:relative;background:var(--white);color:var(--ink);font-family:"Noto Serif JP",serif;}
.abs{position:absolute}
.sans{font-family:"Noto Sans JP",sans-serif}
h1,h2,h3{font-weight:400}

/* hero */
.hero{left:0;top:0;width:1200px;height:665px;
  background:
    radial-gradient(ellipse 70% 22% at 50% 40%,rgba(120,150,170,0.55),rgba(120,150,170,0) 70%),
    radial-gradient(ellipse 60% 30% at 20% 85%,rgba(70,95,40,0.7),rgba(70,95,40,0) 70%),
    radial-gradient(ellipse 55% 30% at 85% 90%,rgba(95,115,55,0.7),rgba(95,115,55,0) 70%),
    linear-gradient(180deg,#b7c9d6 0%,#9bb2c3 18%,#7e98ab 34%,#6d8794 42%,#5c7a6a 50%,#54723f 62%,#4a6833 78%,#3b5628 100%)}
.hero-shade{left:0;top:0;width:1200px;height:665px;background:linear-gradient(180deg,rgba(0,0,0,0.15),rgba(0,0,0,0) 20%,rgba(0,0,0,0) 80%,rgba(0,0,0,0.15))}
.brand{left:32px;top:30px;font-size:26px;letter-spacing:4px;color:var(--white);font-weight:600}
.nav{right:30px;top:38px;display:flex;gap:44px;font-size:14px;color:var(--white);letter-spacing:2px}
.hero-title{left:0;width:1200px;top:250px;text-align:center;color:var(--white);font-size:34px;letter-spacing:6px}
.hero-lead{left:0;width:1200px;top:318px;text-align:center;color:var(--white);font-size:14px;line-height:2.1;letter-spacing:2px}

/* features */
.sec-title{font-size:20px;letter-spacing:3px;display:flex;align-items:baseline;gap:32px}
.sec-title small{font-size:12px;letter-spacing:1px;color:var(--muted)}
.feature-title{left:120px;top:800px}
.feature-text{left:120px;top:860px;width:370px;font-size:12px;line-height:2.2;letter-spacing:1px}
.btn{display:flex;align-items:center;justify-content:center;gap:14px;font-size:12px;letter-spacing:2px;border:1px solid #888;background:var(--white);color:var(--ink)}
.feature-btn{left:296px;top:1080px;width:192px;height:40px}
.feature-photo{left:548px;top:796px;width:652px;height:332px;
  background:
    radial-gradient(ellipse 30% 40% at 45% 60%,rgba(40,80,150,0.55),rgba(40,80,150,0) 70%),
    radial-gradient(ellipse 40% 25% at 70% 20%,rgba(60,110,150,0.5),rgba(60,110,150,0) 70%),
    linear-gradient(180deg,#9aa6ad 0%,#b8c0c4 40%,#8e8f88 70%,#7a756c 100%)}

/* services */
.services{left:0;top:1290px;width:1200px;height:1070px;background:var(--grey-bg)}
.services-title{left:0;width:1200px;top:1400px;justify-content:center}
.services-text{left:120px;width:960px;top:1505px;font-size:12px;line-height:2.2;letter-spacing:1px;text-align:center}
.tile{width:296px;height:252px}
.tile-lead{background:linear-gradient(135deg,#1a86b8,#126a98);color:var(--white);padding:40px 34px}
.tile-lead h3{font-size:18px;letter-spacing:3px;font-weight:600;margin-bottom:22px}
.tile-lead p{font-size:12px;line-height:2.1;letter-spacing:1px}
.t2{background:radial-gradient(circle at 50% 50%,#eef4f7,#b9cfda 60%,#7fa3b6)}
.t3{background:linear-gradient(160deg,#fafbfb 0%,#e3eaee 45%,#c6d3da 60%,#eef2f4 100%)}
.t4{background:radial-gradient(ellipse 30% 45% at 30% 55%,rgba(30,70,140,0.6),rgba(30,70,140,0) 70%),linear-gradient(180deg,#c8ccca,#8a9290 55%,#5f6966)}
.t5{background:radial-gradient(ellipse 60% 40% at 50% 65%,#c9cdd0,#8f979c 60%,#4f5a60)}
.t6{background:radial-gradient(ellipse 40% 30% at 50% 30%,rgba(220,230,230,0.6),rgba(220,230,230,0) 70%),linear-gradient(180deg,#2f4a3a,#5d7568 45%,#6e7b80 100%)}

/* recruit */
.recruit{left:0;top:2360px;width:1200px;height:410px;
  background:
    radial-gradient(ellipse 30% 45% at 85% 40%,rgba(60,55,45,0.55),rgba(60,55,45,0) 70%),
    radial-gradient(ellipse 35% 50% at 12% 55%,rgba(70,70,70,0.5),rgba(70,70,70,0) 70%),
    linear-gradient(120deg,#8c8a85,#b7b2a6 45%,#7c7468)}
.recruit-title{left:0;width:1200px;top:2508px;justify-content:center;color:var(--white)}
.recruit-title small{color:var(--white)}
.recruit-text{left:0;width:1200px;top:2548px;text-align:center;color:var(--white);font-size:18px;line-height:1.9;letter-spacing:3px}
.recruit-btn{left:490px;top:2658px;width:200px;height:38px;background:var(--blue);border:none;color:var(--white)}

/* news */
.news-title{left:88px;top:2970px}
.news-list{left:460px;top:2835px;width:660px;list-style:none;font-size:12px;letter-spacing:1px}
.news-list li{display:flex;gap:28px;line-height:42px}
.news-list time{color:var(--muted)}
.news-btn{left:920px;top:3133px;width:190px;height:38px}

/* contact */
.contact{left:0;top:3290px;width:1200px;height:330px;background:var(--blue)}
.contact-title{left:0;width:1200px;top:3355px;justify-content:center;color:var(--white)}
.contact-title small{color:var(--white)}
.contact-lead{left:0;width:1200px;top:3405px;text-align:center;font-size:13px;letter-spacing:1px;color:var(--white)}
.contact-tel{left:0;width:1200px;top:3462px;display:flex;justify-content:center;align-items:center;gap:14px;color:var(--white)}
.contact-tel strong{font-size:42px;letter-spacing:2px;font-weight:500}
.contact-tel span{font-size:13px;margin-left:8px}

/* footer */
.footer-nav{right:90px;top:3685px;display:flex;gap:60px;font-size:13px;letter-spacing:2px}
.footer-bar{left:0;top:3745px;width:1200px;height:139px;background:var(--footer-bg)}
.footer-brand{left:30px;top:3795px;font-size:24px;letter-spacing:4px;font-weight:600}
.footer-addr{left:415px;top:3807px;font-size:12px;letter-spacing:1px}
</style>
</head>
<body>

<header>
  <div class="abs hero" role="img" aria-label="山並みと草原を望む風景写真"></div>
  <div class="abs hero-shade"></div>
  <div class="abs brand">有限会社青嶺</div>
  <nav class="abs nav sans"><span>ホーム</span><span>お知らせ</span><span>会社案内</span><span>業務内容</span><span>採用情報</span><span>お問い合わせ</span></nav>
  <h1 class="abs hero-title">青嶺は、地域に寄り添う。</h1>
  <p class="abs hero-lead">青嶺は地域の皆さまとともに、確かな技術と誠実な仕事で<br>暮らしを支える会社です。地域の発展を願い、<br>これからも挑戦を続けます。</p>
</header>

<section>
  <h2 class="abs sec-title feature-title">当社の特徴<small>About our company</small></h2>
  <p class="abs feature-text">テキストテキストテキストテキストテキストテキストテキストテキストテキストテキストテキストテキストテキストテキストテキストテキストテキストテキストテキストテキストテキストテキストテキストテキストテキストテキストテキスト</p>
  <div class="abs btn feature-btn"><span>&gt;</span>READ MORE</div>
  <div class="abs feature-photo" role="img" aria-label="工場で作業する作業員の写真"></div>
</section>

<section>
  <div class="abs services"></div>
  <h2 class="abs sec-title services-title">業務内容<small>About our company</small></h2>
  <p class="abs services-text">テキストテキストテキストテキストテキストテキストテキストテキストテキストテキストテキストテキストテキストテキストテキストテキストテキストテキストテキストテキストテキストテキストテキストテキストテキストテキストテキストテキストテキストテキストテキストテキストテキスト</p>
  <div class="abs tile tile-lead" style="left:104px;top:1648px">
    <h3>タイトル</h3>
    <p>テキストテキストテキストテキストテキストテキストテキスト</p>
  </div>
  <div class="abs tile t2" style="left:452px;top:1648px" role="img" aria-label="金属部材の写真"></div>
  <div class="abs tile t3" style="left:800px;top:1648px" role="img" aria-label="金属製品の写真"></div>
  <div class="abs tile t4" style="left:104px;top:1956px" role="img" aria-label="機械で作業する作業員の写真"></div>
  <div class="abs tile t5" style="left:452px;top:1956px" role="img" aria-label="梱包された製品の写真"></div>
  <div class="abs tile t6" style="left:800px;top:1956px" role="img" aria-label="工場内部の写真"></div>
</section>

<section>
  <div class="abs recruit" role="img" aria-label="書類を手に打ち合わせする人物の写真"></div>
  <h2 class="abs sec-title recruit-title">採用情報<small>Recruit</small></h2>
  <p class="abs recruit-text">プロフェッショナルな仕事に誇りを持ち、共に創る。<br>未来を担い、助けあえる仲間と募集！</p>
  <div class="abs btn recruit-btn"><span>&gt;</span>READ MORE</div>
</section>

<section>
  <h2 class="abs sec-title news-title">お知らせ<small>News &amp; Topics</small></h2>
  <ul class="abs news-list sans">
    <li><time>2020.01.01（水）</time>タイトルを記載します。テキストテキストテキストテキスト</li>
    <li><time>2020.01.01（水）</time>タイトルを記載します。テキストテキストテキストテキスト</li>
    <li><time>2020.01.01（水）</time>タイトルを記載します。テキストテキストテキストテキスト</li>
    <li><time>2020.01.01（水）</time>タイトルを記載します。テキストテキストテキストテキスト</li>
    <li><time>2020.01.01（水）</time>タイトルを記載します。テキストテキストテキストテキスト</li>
  </ul>
  <div class="abs btn news-btn"><span>&gt;</span>READ MORE</div>
</section>

<section>
  <div class="abs contact"></div>
  <h2 class="abs sec-title contact-title">お問い合わせ<small>Contact</small></h2>
  <p class="abs contact-lead sans">ご質問やご依頼のご相談など、お気軽にお問い合わせください。</p>
  <div class="abs contact-tel sans">
    <svg width="40" height="40" viewBox="0 0 24 24" aria-hidden="true"><path fill="#ffffff" d="M6.6 10.8c1.4 2.8 3.8 5.1 6.6 6.6l2.2-2.2c.3-.3.7-.4 1-.2 1.1.4 2.3.6 3.6.6.6 0 1 .4 1 1V20c0 .6-.4 1-1 1C10.6 21 3 13.4 3 4c0-.6.4-1 1-1h3.5c.6 0 1 .4 1 1 0 1.3.2 2.5.6 3.6.1.3 0 .7-.2 1l-2.3 2.2z"/></svg>
    <strong>025-000-4721</strong><span>営業時間 10:00 - 17:00</span>
  </div>
</section>

<footer>
  <nav class="abs footer-nav sans"><span>ホーム</span><span>お知らせ</span><span>会社紹介</span><span>業務内容</span><span>採用情報</span><span>お問い合わせ</span></nav>
  <div class="abs footer-bar"></div>
  <div class="abs footer-brand">有限会社青嶺</div>
  <p class="abs footer-addr sans">〒900-0000　新潟県 架空市緑町1番2号　TEL：025-000-4721</p>
</footer>

</body>
</html>
```